Tend Your Harvest - Keep your Bloom - The freedom to choose and participate in your own path to hea

I have a logo that needs to be turned into a large banner for my website. I want to keep the same font in the uploaded logo image. Now this image could stay at the top of the header kind of where it is now on the web site, It doesn't have to be the main thing on the page. I want this header to be artistic - alive, healthy, joyous - colorful banner that shows wellness, healing, vitality and hope.
If you had a chronic illness and came to my site what would you want to see? You'd want to feel empowered, enlightened, engaged, hopeful and feel the love, right?.
I look forward to getting your creative ideas and designs.

Target Market(s)

People struggling with illness who are looking for a better quality of life. We provide training and education on how to do that. Hope, happiness - healing - Vitality - whole natural foods - mediation - visualization - whole health.

Industry/Entity Type

Health And Wellness

Logo Text

Tend Your Harvest with the koru and with Marigold Thwaite (use the font on the uploaded file)

Requirements
Must have
• I've changed the photos in this order. You can pick up options here:
• https://www.filebarrow.example/s/x7pleqnrtwz2kdm/IMG_4402%20%20high%20resolution.jpg?dl=0
• https://www.filebarrow.example/s/m3bvohqyeuc8zta/IMG_4587%20high%20resolution.jpg?dl=0
• My original logo - Tend Your Harvest - Marigold Thwaite
• "Together we make tragic moments magic moments" Join us (sign up type button)
Nice to have
• Something stunningly simple, classy, inviting, where my message gets across.
• Here's a similar website to mine: http://dalvenhope.example
• I need a link to join up somewhere - with my quote.
• "My tragic moments have become magic moments" Join us (sign up type button)
Should not have
• I do not want other people in the header.
• No crunchy granola feel!
• This is gone mainstream now.

```html
<!DOCTYPE html>
<html lang="en">
<head>
<meta charset="utf-8">
<title>Tend Your Harvest – Header Banner</title>
<link rel="stylesheet" href="https://fonts.googleapis.com/css2?family=Cabin:wght@400&family=Great+Vibes&display=swap">
<style>
  :root {
    --bg-white: #ffffff;
    --bg-mint: #eef6e4;
    --leaf-light: #c9ec6a;
    --leaf-mid: #8fcf3a;
    --leaf-deep: #4f8f1e;
    --brand-teal: #6fb5b5;
    --text-grey: #5f5f63;
    --script-blue: #1fa3dd;
    --button-blue: #7dd3f3;
    --button-text: #ffffff;
    --portrait-shirt: #a9dde6;
    --portrait-warm: #f2d7c4;
  }
  html, body {
    margin: 0;
    padding: 0;
    overflow: hidden;
  }
  .banner {
    position: relative;
    width: 1200px;
    height: 440px;
    overflow: hidden;
    background:
      radial-gradient(ellipse 520px 340px at 560px 220px, var(--bg-white) 40%, rgba(255,255,255,0) 100%),
      linear-gradient(90deg, var(--bg-mint) 0%, var(--bg-white) 45%, var(--bg-mint) 100%);
    font-family: "Cabin", "Gill Sans", sans-serif;
  }
  .leaf-photo {
    position: absolute;
    left: 0;
    top: 0;
    width: 380px;
    height: 440px;
    background:
      radial-gradient(ellipse 140px 60px at 230px 200px, var(--leaf-light) 0%, rgba(201,236,106,0) 100%),
      radial-gradient(ellipse 110px 170px at 60px 190px, var(--leaf-mid) 0%, rgba(143,207,58,0) 100%),
      radial-gradient(ellipse 160px 80px at 130px 330px, var(--leaf-mid) 0%, rgba(143,207,58,0) 100%),
      radial-gradient(ellipse 60px 40px at 30px 410px, var(--leaf-deep) 0%, rgba(79,143,30,0) 100%);
    opacity: 0.9;
  }
  .portrait-photo {
    position: absolute;
    right: 0;
    top: 0;
    width: 480px;
    height: 440px;
    background:
      radial-gradient(ellipse 180px 140px at 340px 420px, var(--portrait-shirt) 0%, rgba(169,221,230,0) 100%),
      radial-gradient(ellipse 150px 170px at 390px 170px, var(--portrait-warm) 0%, rgba(242,215,196,0) 100%),
      radial-gradient(ellipse 60px 40px at 320px 20px, var(--leaf-light) 0%, rgba(201,236,106,0) 100%);
  }
  .brand {
    position: absolute;
    left: 412px;
    top: 40px;
    display: flex;
    align-items: center;
    gap: 10px;
    color: var(--brand-teal);
  }
  .brand-mark {
    width: 16px;
    height: 16px;
    border-radius: 50%;
    background: var(--brand-teal);
  }
  .brand-name {
    font-size: 24px;
    line-height: 28px;
    margin: 0;
    font-weight: 400;
  }
  .brand-owner {
    position: absolute;
    left: 438px;
    top: 72px;
    font-size: 20px;
    line-height: 24px;
    color: var(--brand-teal);
    margin: 0;
  }
  .quote {
    margin: 0;
  }
  .quote-line,
  .quote-script {
    position: absolute;
    white-space: nowrap;
    text-align: center;
    line-height: 1;
  }
  .quote-line {
    font-size: 37px;
    color: var(--text-grey);
  }
  .quote-line--top {
    left: 340px;
    width: 370px;
    top: 209px;
  }
  .quote-line--bottom {
    left: 367px;
    width: 370px;
    top: 281px;
  }
  .quote-script {
    left: 336px;
    width: 400px;
    top: 232px;
    font-family: "Great Vibes", cursive;
    font-size: 58px;
    letter-spacing: 2px;
    color: var(--script-blue);
  }
  .quote-flourish {
    position: absolute;
    left: 0;
    top: 0;
    width: 1200px;
    height: 440px;
    pointer-events: none;
  }
  .signup-button {
    position: absolute;
    left: 421px;
    top: 346px;
    width: 221px;
    height: 52px;
    background: var(--button-blue);
    color: var(--button-text);
    font-size: 24px;
    line-height: 52px;
    text-align: center;
    text-decoration: none;
  }
</style>
</head>
<body>
  <header class="banner">
    <div class="leaf-photo" role="img" aria-label="Fresh green leaves on a soft blurred background"></div>
    <div class="portrait-photo" role="img" aria-label="Portrait of the founder in a light turquoise shirt"></div>

    <div class="brand">
      <span class="brand-mark"></span>
      <p class="brand-name">Tend Your Harvest</p>
    </div>
    <p class="brand-owner">Marigold Thwaite</p>

    <svg class="quote-flourish" viewBox="0 0 1200 440" aria-hidden="true">
      <path d="M316 241 Q340 239 368 240" stroke="#1fa3dd" stroke-width="1.5" fill="none"/>
      <path d="M688 240 Q718 238 748 241" stroke="#1fa3dd" stroke-width="1.5" fill="none"/>
    </svg>

    <p class="quote">
      <span class="quote-line quote-line--top">"Together we make</span>
      <span class="quote-script">tragic moments</span>
      <span class="quote-line quote-line--bottom">magic moments"</span>
    </p>

    <a class="signup-button" href="#join">Sign Up Today</a>
  </header>
</body>
</html>
```